Community Legal Website

The website is about a law in legal area (Fiscal), it has a moderator and the community also contributes with information.

Attention that this is not for a Law Firm. This is a community site where all the lawyers can contribute wiith their knowledge and at the same time where they can read the Official Law in the fiscal area.

The site is in portuguese, but we have attach information in english about the functionalities.

I attach information which represents the first version of the site done by html.. That is the site we intend to improve.

The site is quite simple because the main pages are:
- Home page;
- Section page (which has the Chapters and articles)
- Article page;

This pages all belong to the article:

redaccao_actual.htm, redaccoes_anteriores.htm, anotacoes.htm, jurisprudencia.htm, decisoesadministrativas.htm, minutas.htm, duvidas.htm

AS you see in all of them the options are always there.

The most important in this site is the usability of the content:

The FAQ, Contacts, Terms of conditions, who we are, are links less important.

Also there is a possibility to have in the homepage a higligh of certain articles that we want to raise from the others.

Please check the excel sheet as well as the zip file wich has the site in portuguese that you can use a website translator to check in your language.
Updates

We added a excel sheet with the functionalities in english which the site must have.

Reason: Because this is easter time we have increased the time for the deliver

Please check briefing update.

Reason: There were some request to extend the deadline because of the Easter

Hi!

Please read carefully the briefing. People are presenting me company web sites adn this is NOT a company web site. THis is a Site wich has a content of Laws. Please check the 1st version in the zip file and improve it. The options are there and you can translate in google tradutor or reading the excel sheet attach.

txs,
KM

Reason: My client need more desing choices

Target Market(s)

Lawyers, jurists and people related with the fiscal Law.

Industry/Entity Type

Legal

Requirements
Must have
• The interface should be clean and elegant.
It should also contribute to speed.
And try to avoid to many distract elements.
The site will be dinamic and with a backoffice, so in that you have to be carefully with the space dynamic. But you don't have to worry about the backoffice. Only the front office which is the public site.

```html
<!DOCTYPE html>
<html lang="pt">
<head>
<meta charset="utf-8">
<title>PEREIRA NUNES.net — Legislação Anotada</title>
<link rel="stylesheet" href="https://fonts.googleapis.com/css2?family=Open+Sans:ital,wght@0,300;0,400;0,600;0,700;1,400;1,700&display=swap">
<style>
:root{
  --teal-dark:#4d766f;
  --teal:#6a928b;
  --teal-soft:#8fb1ab;
  --row:#eef5f4;
  --row-active:#d9e8e5;
  --text-strong:#3d5c57;
  --text-link:#4f7a73;
  --ink:#222;
  --grey-bar:#dcdcdc;
  --footer:#e8e8e8;
  --footer-text:#7a7a7a;
  --white:#fff;
}
*{margin:0;padding:0;box-sizing:border-box}
html,body{width:1200px;height:682px;overflow:hidden;background:var(--white);font-family:"Open Sans",Arial,sans-serif}
.page{position:relative;width:1200px;height:682px}
.top-strip{position:absolute;left:0;top:0;width:1200px;height:5px;background:var(--grey-bar)}
.contact-tab{position:absolute;left:850px;top:0;width:100px;height:18px;background:var(--teal-soft);transform:skewX(-18deg);display:flex;align-items:center;justify-content:center}
.contact-tab span{transform:skewX(18deg);color:var(--white);font-style:italic;font-size:11px;letter-spacing:.3px}
.brand{position:absolute;left:250px;top:60px;display:flex;align-items:center;gap:10px}
.brand-mark{width:18px;height:18px;background:var(--teal-dark)}
.brand-name{font-size:14px;color:var(--ink);font-weight:400}
.main-nav{position:absolute;right:258px;top:40px;height:62px;display:flex;align-items:center}
.main-nav a{font-size:11.5px;color:var(--ink);text-decoration:none;padding:0 12px;position:relative}
.main-nav a.is-active{color:var(--teal)}
.main-nav .divider{width:14px;height:62px;background:linear-gradient(to right,rgba(0,0,0,.06),rgba(0,0,0,0));transform:skewX(-14deg)}
.hero{position:absolute;left:232px;top:123px;width:735px;height:202px;background:linear-gradient(100deg,#f3f4f4 0%,#e8ebec 35%,#d8d6d3 55%,#c9b9ad 75%,#d9dfe4 100%)}
.hero-caption{position:absolute;left:21px;top:68px;width:251px;height:82px;background:var(--teal-soft);padding:10px 0 0 19px}
.hero-caption h1{font-weight:300;font-size:31px;color:var(--white);line-height:1.1;letter-spacing:.3px}
.hero-caption p{font-size:10px;font-style:italic;font-weight:700;color:#1f2a28;margin:2px 0 0 30px}
.hero-pointer{position:absolute;left:272px;top:118px}
.law-panel{position:absolute;top:348px;width:359px}
.law-panel--fiscal{left:232px}
.law-panel--admin{left:608px}
.law-panel header{height:38px;background:linear-gradient(to right,var(--teal-dark),var(--teal));display:flex;align-items:center;justify-content:space-between;padding:0 9px 0 24px}
.law-panel h2{font-weight:400;font-size:15.5px;color:var(--white);letter-spacing:.2px}
.law-list{list-style:none}
.law-list li{background:var(--row);height:42px;border-bottom:2px solid var(--white);padding:9px 0 0 14px;display:flex;gap:6px}
.law-list li.is-active{background:var(--row-active)}
.law-list li.is-active .law-text{text-decoration:underline}
.doc-icon{margin-top:1px;flex:none}
.law-text{font-size:10px;line-height:12px;color:var(--text-link)}
.law-text strong{display:block;font-weight:700;color:var(--text-strong)}
.panel-shade{height:60px;background:linear-gradient(to bottom,rgba(0,0,0,.03),rgba(0,0,0,0))}
.law-panel--admin .panel-shade{height:192px;background:linear-gradient(to right,rgba(0,0,0,.05),rgba(0,0,0,0) 4%)}
.law-panel--fiscal .panel-shade{background:linear-gradient(to right,rgba(0,0,0,.05),rgba(0,0,0,0) 4%,rgba(0,0,0,0) 96%,rgba(0,0,0,.04))}
.site-footer{position:absolute;left:0;top:622px;width:1200px;height:60px;background:var(--footer);border-top:2px solid #d6d6d6;text-align:center;padding-top:19px;font-size:10px;color:var(--footer-text)}
</style>
</head>
<body>
<div class="page">
  <div class="top-strip"></div>
  <a class="contact-tab"><span>CONTACTOS</span></a>

  <div class="brand">
    <span class="brand-mark"></span>
    <span class="brand-name">PEREIRA NUNES.net</span>
  </div>

  <nav class="main-nav">
    <a>TERMOS DE UTILIZAÇÃO</a>
    <span class="divider"></span>
    <a class="is-active">PERGUNTAS FREQUENTES</a>
    <span class="divider"></span>
    <a>QUEM SOMOS</a>
  </nav>

  <section class="hero" role="img" aria-label="Fotografia de uma equipa de profissionais sorridentes num escritório luminoso">
    <div class="hero-caption">
      <h1>LOREM IPSUM</h1>
      <p>dolor sit amet consectetur adipisicing</p>
    </div>
    <svg class="hero-pointer" width="50" height="24" viewBox="0 0 50 24"><polygon points="0,0 50,22 0,24" fill="#8fb1ab"/></svg>
  </section>

  <section class="law-panel law-panel--fiscal">
    <header>
      <h2>LEGISLAÇÃO FISCAL ANOTADA</h2>
      <svg width="26" height="24" viewBox="0 0 26 24" fill="none" stroke="#fff" stroke-width="1.2">
        <rect x="1" y="1" width="24" height="22" rx="2" opacity=".5"/>
        <path d="M6 19V10M10 19V6M14 19V11M18 19V8M21 19v-5" stroke-width="2.2"/>
        <path d="M3 20.5h20"/>
      </svg>
    </header>
    <ul class="law-list">
      <li><svg class="doc-icon" width="8" height="10" viewBox="0 0 8 10"><rect x=".5" y=".5" width="7" height="9" fill="none" stroke="#8a9a97"/><path d="M2 3h4M2 5h4M2 7h4" stroke="#8a9a97"/></svg>
        <span class="law-text"><strong>Código do IRS</strong>Imposto sobre o Rendimento das Pessoas Singulares</span></li>
      <li class="is-active"><svg class="doc-icon" width="8" height="10" viewBox="0 0 8 10"><rect x=".5" y=".5" width="7" height="9" fill="none" stroke="#8a9a97"/><path d="M2 3h4M2 5h4M2 7h4" stroke="#8a9a97"/></svg>
        <span class="law-text"><strong>Código do IRC</strong>Imposto sobre o Rendimento das Pessoas Colectivas</span></li>
      <li><svg class="doc-icon" width="8" height="10" viewBox="0 0 8 10"><rect x=".5" y=".5" width="7" height="9" fill="none" stroke="#8a9a97"/><path d="M2 3h4M2 5h4M2 7h4" stroke="#8a9a97"/></svg>
        <span class="law-text"><strong>Código do IMI</strong>Imposto Municipal sobre Imóveis</span></li>
      <li><svg class="doc-icon" width="8" height="10" viewBox="0 0 8 10"><rect x=".5" y=".5" width="7" height="9" fill="none" stroke="#8a9a97"/><path d="M2 3h4M2 5h4M2 7h4" stroke="#8a9a97"/></svg>
        <span class="law-text"><strong>RCPIT</strong>Regulamento Complementar do Procedimento de Inspecção Tributária</span></li>
    </ul>
    <div class="panel-shade"></div>
  </section>

  <section class="law-panel law-panel--admin">
    <header>
      <h2>LEGISLAÇÃO ADMINISTRATIVA ANOTADA</h2>
      <svg width="22" height="24" viewBox="0 0 22 24" fill="none" stroke="#fff" stroke-width="1.2">
        <rect x="1" y="1" width="20" height="22" rx="2"/>
        <path d="M5 6h2M9 6h8M5 10h2M9 10h8M5 14h2M9 14h8M5 18h2M9 18h8" stroke-width="1.6"/>
      </svg>
    </header>
    <ul class="law-list">
      <li><svg class="doc-icon" width="8" height="10" viewBox="0 0 8 10"><rect x=".5" y=".5" width="7" height="9" fill="none" stroke="#8a9a97"/><path d="M2 3h4M2 5h4M2 7h4" stroke="#8a9a97"/></svg>
        <span class="law-text"><strong>CPTA</strong>Código do Procedimento nos Tribunais Administrativos</span></li>
    </ul>
    <div class="panel-shade"></div>
  </section>

  <footer class="site-footer">(c) PEREIRA NUNES - 2013</footer>
</div>
</body>
</html>
```